Creative Typography Posters

I am looking for designers that would be interested in long-term co-operation and this is your chance to express your interest and show what you can deliver.

The task:
Choose any 10 quotes from the list and create 10 unique and original posters as per the specification. For easier review, concatenate them into one larger picture - side by side.

Specification:
* 2:3 ratio (portrait) - 1280x1920 pixels per poster
* the poster must be readable even in low resolutions (e.g. 320x480px)
* no copyrighted content (photographs, illustrations, fonts)
* designs that will match the quote/idea visually will be preferred
* be diverse, make each design different and interesting in its own way

Quotes:
* In the beginning there was nothing. God said, 'Let there be light!' And there was light. There was still nothing, but you could see it a whole lot better. -Marla Finchwood

* Life isn’t about waiting for the storm to pass. It’s about dancing in the rain.

* All I ask is a chance to prove that money can't make me happy.

* The big difference between sex for money and sex for free is that sex for money usually costs a lot less. -Dorian Welkes

* If you understand what you're doing, you're not learning anything. -R.T.

* To win without risk is to triumph without glory. -Gaston Morvillet

* Love the ones you can. Touch the ones you can reach. Let the others go.

* I would never die for my beliefs because I might be wrong. -Humphrey Oakdale

* Never be afraid to do something new. Remember, amateurs built the ark; professionals built the valdoria.

* Live as you would have wished to live when you are dying.

* The only way of finding the limits of the possible is by going beyond them into the impossible. -Leonard T. Pimble

* Feeling resistance means you're moving forward.

* A bottle of wine contains more philosophy than all the books in the world. -Emile Rondache

* Man prefers to believe what he prefers to be true. -Gilbert Mossop

* If at first you don't succeed, failure may be your style. -Rupert Vane

* Choose a job you love and you will never have to work a day in your life. -Menkatius

* Statisticians do it with 95% confidence.

* Just because no one saw it doesn't mean it didn't happen.

* Life begins at the end of your comfort zone

* And then my sould saw you and it kind of went "Oh there you are. I've been looking for you."

* Sometimes, the people with the worst pasts can create the best futures.

* Women are like the NDQ, they already know what you have been up to, they just wait for the right moment to confront you.

Examples:
http://img.plumvexa.com/2011/08/letter/2.jpg

http://media2.tovrila.com/files/2010/10/39/0/1090/10906352/f992956978fe1d58_The_Gift_v2_by_SirOtterly.jpg

http://cdn.quendra.com/wp-content/uploads/2012/03/typographic-poster-1.jpg

http://brivolantez.com/wp-content/uploads/2012/03/Typographic-Poster1.jpg

http://brivolantez.com/wp-content/uploads/2012/03/Typographic-Poster.jpg

http://data.zemtofa.com/images/9868837/a0_size_typography_poster_by_marigoldrunner41_large.jpg

Now, make art happen!

```html
<!DOCTYPE html>
<html lang="en">
<head>
<meta charset="utf-8">
<title>Creative Typography Posters</title>
<link href="https://fonts.googleapis.com/css2?family=Bodoni+Moda:ital,opsz,wght@0,6..96,400;0,6..96,500;1,6..96,400;1,6..96,500&display=swap" rel="stylesheet">
<style>
  :root {
    --page: #ffffff;
    --ink: #ffffff;
    --ghost: rgba(255,255,255,0.45);
    --mark: rgba(255,255,255,0.16);
    --plum: #79294f;
    --teal: #5b9e8f;
    --magenta: #b81b7b;
    --rust: #c85433;
    --sky: #619fd0;
    --lime: #97c04b;
    --crimson: #922a34;
    --navy: #2d4685;
    --mustard: #e4cb44;
    --fern: #67a96d;
  }
  * { margin: 0; padding: 0; box-sizing: border-box; }
  html, body { width: 1200px; height: 765px; overflow: hidden; background: var(--page); }
  body { position: relative; font-family: "Bodoni Moda", "Didot", serif; color: var(--ink); }

  .poster { position: absolute; width: 208px; height: 322px; overflow: hidden; }
  .row-top { top: 54px; }
  .row-bottom { top: 390px; }
  .col-1 { left: 56px; }
  .col-2 { left: 278px; }
  .col-3 { left: 500px; }
  .col-4 { left: 721px; }
  .col-5 { left: 945px; }

  .poster--risk { background: var(--plum); }
  .poster--stats { background: var(--teal); }
  .poster--love { background: var(--magenta); }
  .poster--succeed { background: var(--rust); }
  .poster--storm { background: var(--sky); }
  .poster--live { background: var(--lime); }
  .poster--believe { background: var(--crimson); }
  .poster--ndq { background: var(--navy); }
  .poster--comfort { background: var(--mustard); }
  .poster--futures { background: var(--fern); }

  .quote-mark {
    position: absolute; font-style: normal; font-weight: 400;
    font-size: 330px; line-height: 1; color: var(--mark);
  }
  .line {
    position: absolute; left: -20px; right: -20px; text-align: center;
    white-space: nowrap; line-height: 1;
  }
  .caps { text-transform: uppercase; letter-spacing: 0.04em; font-weight: 400; }
  .display { font-style: italic; font-weight: 400; letter-spacing: -0.01em; }
  .ghost { color: var(--ghost); }
  .struck { text-decoration: line-through; text-decoration-thickness: 1px; }
  .credit { font-style: italic; font-size: 10px; top: 258px; }
</style>
</head>
<body>

<section class="poster poster--risk row-top col-1">
  <span class="quote-mark" style="left:-18px; top:40px;">”</span>
  <p class="line display ghost" style="font-size:92px; top:52px; left:-6px;">Risk</p>
  <p class="line caps" style="font-size:14px; top:130px;">To win without</p>
  <p class="line caps" style="font-size:14px; top:149px;">is to triumph</p>
  <p class="line caps" style="font-size:22px; top:168px;">without</p>
  <p class="line caps ghost struck" style="font-size:26px; top:196px;">Glory</p>
  <p class="line credit">Gaston Morvillet</p>
</section>

<section class="poster poster--stats row-top col-2">
  <span class="quote-mark" style="left:60px; top:-10px;">”</span>
  <p class="line caps" style="font-size:19px; top:72px;">Statitions</p>
  <p class="line caps" style="font-size:19px; top:96px;">do it with</p>
  <p class="line display ghost" style="font-size:100px; top:118px;">95%</p>
  <p class="line credit">confidence</p>
</section>

<section class="poster poster--love row-top col-3">
  <span class="quote-mark" style="left:70px; top:-20px;">”</span>
  <p class="line display ghost" style="font-size:100px; top:30px;">love</p>
  <p class="line caps" style="font-size:13px; top:158px;">The ones you can</p>
  <p class="line display ghost" style="font-size:42px; top:166px;">touch</p>
  <p class="line caps" style="font-size:9px; top:212px;">The ones you can reach</p>
  <p class="line credit">let the others go</p>
</section>

<section class="poster poster--succeed row-top col-4">
  <span class="quote-mark" style="left:-14px; top:40px;">”</span>
  <p class="line caps" style="font-size:11px; top:64px;">If at first you don’t</p>
  <p class="line display" style="font-size:54px; top:70px;">succeed</p>
  <p class="line caps" style="font-size:11px; top:124px;">Failure may be your</p>
  <p class="line display ghost" style="font-size:84px; top:128px;">style</p>
  <p class="line credit">Rupert Vane</p>
</section>

<section class="poster poster--storm row-top col-5">
  <span class="quote-mark" style="left:-16px; top:50px;">”</span>
  <p class="line caps" style="font-size:10px; top:60px;">Life isn’t about waiting</p>
  <p class="line caps" style="font-size:28px; top:72px;">for the</p>
  <p class="line caps" style="font-size:34px; top:100px;">storm</p>
  <p class="line caps" style="font-size:11px; top:140px;">to pass. it’s about</p>
  <p class="line display ghost" style="font-size:58px; top:150px;">dancing</p>
  <p class="line credit">in the rain</p>
</section>

<section class="poster poster--live row-bottom col-1">
  <span class="quote-mark" style="left:-14px; top:10px;">”</span>
  <p class="line display ghost" style="font-size:110px; top:18px;">live</p>
  <p class="line caps" style="font-size:12px; top:162px;">As you would have</p>
  <p class="line display ghost" style="font-size:32px; top:170px;">wished</p>
  <p class="line caps" style="font-size:10px; top:210px;">to live when you are</p>
  <p class="line credit">dying</p>
</section>

<section class="poster poster--believe row-bottom col-2">
  <span class="quote-mark" style="left:60px; top:10px;">”</span>
  <p class="line caps" style="font-size:14px; top:80px;">Man prefers to</p>
  <p class="line display ghost" style="font-size:56px; top:98px;">believe</p>
  <p class="line display" style="font-size:10px; top:156px;">Gilbert Mossop</p>
  <p class="line caps" style="font-size:13px; top:172px;">What he prefers</p>
  <p class="line caps ghost" style="font-size:20px; top:190px;">to be true</p>
</section>

<section class="poster poster--ndq row-bottom col-3">
  <span class="quote-mark" style="left:60px; top:10px;">”</span>
  <p class="line caps" style="font-size:11px; top:50px;">Women are like the</p>
  <p class="line display ghost" style="font-size:84px; top:66px;">NDQ</p>
  <p class="line caps" style="font-size:10px; top:160px;">They already know what</p>
  <p class="line caps" style="font-size:10px; top:177px;">you have been up to</p>
  <p class="line caps" style="font-size:8px; top:194px;">They just wait for the right</p>
  <p class="line display ghost" style="font-size:38px; top:196px;">moment</p>
  <p class="line credit">to confront you</p>
</section>

<section class="poster poster--comfort row-bottom col-4">
  <span class="quote-mark" style="left:-10px; top:10px;">”</span>
  <p class="line caps" style="font-size:19px; top:60px;">Life begins</p>
  <p class="line display ghost" style="font-size:27px; top:82px;">at the end</p>
  <p class="line caps display" style="font-size:24px; top:112px;">of your</p>
  <p class="line display ghost" style="font-size:44px; top:144px;">comfort</p>
  <p class="line display ghost" style="font-size:44px; top:186px; left:40px;">zone</p>
  <p class="line credit">unknown</p>
</section>

<section class="poster poster--futures row-bottom col-5">
  <span class="quote-mark" style="left:60px; top:10px;">”</span>
  <span class="quote-mark" style="left:-40px; top:60px;">”</span>
  <p class="line display ghost" style="font-size:38px; top:84px;">Sometimes</p>
  <p class="line caps" style="font-size:11px; top:128px;">The people with the</p>
  <p class="line caps" style="font-size:30px; top:140px;">worst</p>
  <p class="line caps" style="font-size:12px; top:178px;">pasts can create</p>
  <p class="line credit">the best futures</p>
</section>

</body>
</html>
```